Redesign retirement planner website

Provide an original design for a website. The site should introduce the retirement planner, explain the basic offerings of his services, and invite the website visitor to enter their name, phone, and email. Please provide a ready-to-publish redesign that can actually be published via a Wordpress template or other major website builder like SquareSpace or Wix. Some introductory content is attached, but feel free to add additional sections/images/blocks/copywriting and rearrange/delete sections entirely to make your design original and compelling. Feel free to pull copywriting from here but again, do not use this original design, feel free to create an entirely NEW design and layout. lynx-mango-trel (dot) sitefolio (dot) com password: 1234 -- FINAL NOTE: Do not choose a stock photo of a man for the retirement planner. This website needs to work well with no photo of the retirement planner himself. Think of a non-face-focused design to win this competition.

Industry/Entity Type

Retirement planner personal website

Number of Pages Required

1 page

Font styles to use
Sans Serif
Decorative

Requirements
Must have
• Please provide a ready-to-publish redesign that can actually be published via a Wordpress template or other major website builder.

```html
<!DOCTYPE html>
<html lang="en">
<head>
<meta charset="utf-8">
<title>Dalton Mercer – Retirement Specialist</title>
<link href="https://fonts.googleapis.com/css2?family=Poppins:wght@400;500;600;700&display=swap" rel="stylesheet">
<style>
:root{
  --gold:#f5c400;
  --gold-dark:#e0b000;
  --cream:#fff7d9;
  --ink:#222222;
  --muted:#555555;
  --footer:#3b3b3b;
  --footer-deep:#2f2f2f;
  --white:#ffffff;
}
*{box-sizing:border-box;margin:0;padding:0}
html,body{width:1200px;height:3228px;overflow:hidden}
body{font-family:"Poppins",sans-serif;color:var(--ink);background:var(--white);position:relative}

/* hero */
.hero{position:absolute;left:0;top:0;width:1200px;height:745px;
  background:linear-gradient(180deg,#7f8f8a 0%,#a9b39a 30%,#c9c48a 45%,#5d7a3a 60%,#3d5a24 80%,#2b4119 100%)}
.nav{position:absolute;left:0;top:0;width:1200px;height:60px;display:flex;align-items:center;padding:0 44px 0 48px}
.brand{font-weight:700;font-size:24px;color:var(--gold)}
.nav-links{margin-left:auto;display:flex;align-items:center;gap:26px;font-size:15px;font-weight:500;color:var(--gold)}
.btn{display:inline-block;background:var(--gold);color:var(--ink);font-weight:600;border-radius:6px;font-size:15px}
.nav .btn{padding:8px 18px}
.hero-title{position:absolute;left:0;width:1200px;top:296px;text-align:center;color:var(--gold);font-weight:700;font-size:62px;line-height:1.12}
.hero-sub{position:absolute;left:0;width:1200px;top:452px;text-align:center;color:var(--white);font-size:16px}
.hero-foot{position:absolute;left:0;width:1200px;top:680px;text-align:center;color:var(--white);font-size:13px}
.hero-chev{position:absolute;left:588px;top:708px}

/* about */
.about-photo{position:absolute;left:92px;top:832px;width:408px;height:408px;border-radius:8px;
  background:linear-gradient(135deg,#8a5a3a,#c8a47a 50%,#5c3a26)}
.about-text{position:absolute;left:610px;top:832px;width:510px}
.section-h{color:var(--gold);font-weight:700}
.about-text h2{font-size:27px;line-height:1.25;margin-bottom:24px}
.about-text p{font-size:15px;line-height:1.6;margin-bottom:36px}
.about-text .btn{padding:9px 20px}

/* specialties */
.center-h{position:absolute;left:0;width:1200px;text-align:center;font-size:30px}
.cards{position:absolute;left:90px;top:1390px;width:1020px;display:flex;gap:16px}
.card{flex:1;height:262px;background:var(--cream);border-radius:6px;padding:20px 14px;text-align:center}
.card svg{display:block;margin:0 auto 12px}
.card h3{font-size:17px;font-weight:600;margin-bottom:8px}
.card p{font-size:12.5px;line-height:1.5}
.arrow{position:absolute;width:28px;height:28px;border-radius:50%;background:var(--white);box-shadow:0 1px 4px rgba(0,0,0,.25);display:flex;align-items:center;justify-content:center}

/* testimonials */
.reviews{position:absolute;left:90px;top:1872px;width:1020px;display:flex;gap:20px}
.review{flex:1;padding:20px 20px 24px;border-radius:6px}
.review.featured{background:var(--white);box-shadow:0 4px 18px rgba(0,0,0,.14)}
.review h4{font-size:17px;font-weight:600;margin-bottom:10px}
.stars{display:flex;gap:6px;margin-bottom:14px}
.review p{font-size:14px;line-height:1.55}
.dots{position:absolute;left:548px;top:2152px;display:flex;gap:20px}
.dot{width:28px;height:28px;border-radius:50%;background:var(--white);box-shadow:0 1px 4px rgba(0,0,0,.25);display:flex;align-items:center;justify-content:center}

/* contact form */
.form-h{position:absolute;left:0;width:1200px;top:2286px;text-align:center;font-size:32px}
.form-sub{position:absolute;left:0;width:1200px;top:2338px;text-align:center;font-size:18px;font-weight:500}
.form{position:absolute;left:372px;top:2380px;width:456px}
.label{font-size:14px;font-weight:500;margin-bottom:8px}
.row{display:flex;gap:16px;margin-bottom:28px}
.field{height:42px;border:1px solid var(--gold);border-radius:4px;padding:0 12px;font-size:13px;color:#aaa;display:flex;align-items:center;flex:1}
.field.full{margin-bottom:28px}
.check{display:flex;align-items:center;gap:10px;font-size:13px;margin-bottom:26px}
.box{width:18px;height:18px;border-radius:3px;background:var(--gold);display:flex;align-items:center;justify-content:center}
.form .btn{display:block;text-align:center;padding:12px 0;margin-top:8px}

/* footer */
.footer{position:absolute;left:0;top:2860px;width:1200px;height:368px;background:var(--footer)}
.footer .brand{position:absolute;left:88px;top:34px;font-size:38px}
.f-info{position:absolute;left:88px;top:112px;color:var(--white);font-size:14px;line-height:2.4}
.social{position:absolute;left:88px;top:222px;display:flex;gap:14px}
.social span{width:20px;height:20px;border-radius:50%;background:var(--white)}
.f-col{position:absolute;top:40px;color:var(--white)}
.f-col h5{font-size:17px;font-weight:600;margin-bottom:16px}
.f-col a{display:block;font-size:14px;color:var(--white);text-decoration:none;line-height:2.3}
.copy{position:absolute;left:0;bottom:0;width:1200px;height:44px;background:var(--footer-deep);color:#d8d8d8;font-size:12px;text-align:center;line-height:44px;border-top:1px solid #555}
</style>
</head>
<body>

<header class="hero" role="img" aria-label="Photo of an elderly couple walking across a sunlit green field at sunset">
  <nav class="nav">
    <div class="brand">Dalton Mercer</div>
    <div class="nav-links">
      <span>Home</span><span>About Us</span><span>Specialties</span>
      <span class="btn">Contact Me</span>
    </div>
  </nav>
  <h1 class="hero-title">I'm a Counselor &amp;<br>Retirement Specialist</h1>
  <p class="hero-sub">Let's plan your retirement with me</p>
  <p class="hero-foot">Don't Leave Your Retirement to Chance</p>
  <svg class="hero-chev" width="24" height="16" viewBox="0 0 24 16"><path d="M4 4l8 8 8-8" fill="none" stroke="#fff" stroke-width="3"/></svg>
</header>

<section class="about">
  <div class="about-photo" role="img" aria-label="Photo of a retired gentleman seated in a warm, wood-panelled room"></div>
  <div class="about-text">
    <h2 class="section-h">Thoughtful and Meaningful<br>Retirement Planning</h2>
    <p>You have a lifetime of accomplishments. Learning about them is my extraordinary honor. When I meet clients to make a plan for their lives of work and savings, I understand my solemn privilege. Your capital is irreplaceable. My job is to maximize its benefit for your health, family, and legacy.</p>
    <span class="btn">Contact Me</span>
  </div>
</section>

<section class="specialties">
  <h2 class="center-h section-h" style="top:1318px">My Specialties</h2>
  <div class="arrow" style="left:50px;top:1506px"><svg width="10" height="10" viewBox="0 0 10 10"><path d="M7 0L2 5l5 5z" fill="#222"/></svg></div>
  <div class="arrow" style="left:1122px;top:1506px"><svg width="10" height="10" viewBox="0 0 10 10"><path d="M3 0l5 5-5 5z" fill="#222"/></svg></div>
  <div class="cards">
    <article class="card">
      <svg width="30" height="30" viewBox="0 0 30 30"><rect x="4" y="6" width="18" height="20" rx="2" fill="none" stroke="#e0b000" stroke-width="2.5"/><path d="M24 4l3 3-10 10-4 1 1-4z" fill="#e0b000"/></svg>
      <h3>Estate Planning</h3>
      <p>Ensure your legacy is protected with comprehensive estate planning. I will guide you through creating wills, trusts, and other essential documents to secure your assets for future generations, ensuring your wishes are honored.</p>
    </article>
    <article class="card">
      <svg width="30" height="30" viewBox="0 0 30 30"><path d="M3 12l12-8 12 8v14H3z" fill="#e0b000"/><rect x="7" y="14" width="16" height="3" fill="#fff7d9"/></svg>
      <h3>Retirement forecasting</h3>
      <p>Plan for a fulfilling retirement with our expert forecasting services. I will analyze your financial situation and future needs to develop a personalized strategy, helping you achieve your retirement goals with confidence.</p>
    </article>
    <article class="card">
      <svg width="30" height="30" viewBox="0 0 30 30"><path d="M15 3a12 12 0 1 0 12 12H15z" fill="#e0b000"/><path d="M18 0a12 12 0 0 1 12 12H18z" fill="#e0b000"/></svg>
      <h3>Final expense</h3>
      <p>Prepare for life's final expenses with peace of mind. My services help you plan for costs associated with end-of-life arrangements, alleviating financial stress for your loved ones during a difficult time.</p>
    </article>
    <article class="card">
      <svg width="30" height="30" viewBox="0 0 30 30"><circle cx="15" cy="9" r="5" fill="#e0b000"/><path d="M4 22c4-3 8-3 11 0 3-3 7-3 11 0v4H4z" fill="#e0b000"/></svg>
      <h3>Life insurance</h3>
      <p>Safeguard your family's future with tailored life insurance solutions. I provide expert advice to help you choose the right coverage, ensuring financial security for your loved ones when they need it most.</p>
    </article>
  </div>
</section>

<section class="testimonials">
  <h2 class="center-h section-h" style="top:1708px;font-size:27px">Customer Satisfaction is Our Top Priority</h2>
  <div class="reviews">
    <article class="review">
      <h4>Janet &amp; Paul Whitford</h4>
      <div class="stars"><svg width="130" height="20" viewBox="0 0 130 20"><g fill="#f5c400"><path id="s" d="M10 1l2.6 6 6.4.5-4.9 4.2 1.5 6.3L10 14.7 4.4 18l1.5-6.3L1 7.5 7.4 7z"/><use href="#s" x="27"/><use href="#s" x="54"/><use href="#s" x="81"/><use href="#s" x="108"/></g></svg></div>
      <p>"Dalton has been a guiding light in our retirement planning. His careful approach helped us feel confident about our future. We now have a clear path to enjoy our golden years without financial worries."</p>
    </article>
    <article class="review featured">
      <h4>Gregory Lansing</h4>
      <div class="stars"><svg width="130" height="20" viewBox="0 0 130 20"><g fill="#f5c400"><use href="#s"/><use href="#s" x="27"/><use href="#s" x="54"/><use href="#s" x="81"/><use href="#s" x="108"/></g></svg></div>
      <p>"Working with Dalton was a game changer. He took the time to understand our unique situation and designed a plan that truly reflects our needs and goals. We couldn't be happier with the peace of mind he's given us."</p>
    </article>
    <article class="review">
      <h4>Harold &amp; Mae Corbin</h4>
      <div class="stars"><svg width="130" height="20" viewBox="0 0 130 20"><g fill="#f5c400"><use href="#s"/><use href="#s" x="27"/><use href="#s" x="54"/><use href="#s" x="81"/><use href="#s" x="108"/></g></svg></div>
      <p>"Thanks to Dalton's expertise, we've optimized our savings, and now we feel secure about our health and family's future. His professionalism and dedication are unmatched."</p>
    </article>
  </div>
  <div class="dots">
    <div class="dot"><svg width="10" height="10" viewBox="0 0 10 10"><path d="M7 0L2 5l5 5z" fill="#222"/></svg></div>
    <div class="dot"><svg width="10" height="10" viewBox="0 0 10 10"><path d="M3 0l5 5-5 5z" fill="#222"/></svg></div>
  </div>
</section>

<section class="contact">
  <h2 class="form-h section-h">Allow me to introduce myself</h2>
  <p class="form-sub">Let's plan for golden memories.</p>
  <form class="form">
    <div class="label">Name *</div>
    <div class="row"><div class="field">First</div><div class="field">Last</div></div>
    <div class="label">Email *</div>
    <div class="field full"></div>
    <div class="check"><span class="box"><svg width="12" height="10" viewBox="0 0 12 10"><path d="M1 5l3 3 7-7" fill="none" stroke="#fff" stroke-width="2"/></svg></span>Sign up for news and updates</div>
    <div class="label">Phone</div>
    <div class="field full"></div>
    <span class="btn">Say Hi!</span>
  </form>
</section>

<footer class="footer">
  <div class="brand">Dalton Mercer</div>
  <div class="f-info">dmercer@mercerplanning.com<br>(415) 555-0132</div>
  <div class="social"><span></span><span></span></div>
  <div class="f-col" style="left:610px"><h5>Menu</h5><a>Home</a><a>Specialties</a></div>
  <div class="f-col" style="left:868px"><h5>About Us</h5><a>Contact Us</a><a>FAQ</a><a>Terms of Service</a><a>Privacy Policy</a></div>
  <div class="copy">© Copyright - Dalton Mercer 2024</div>
</footer>

</body>
</html>
```